Business Card Design

I would like a new business card design for an accounting firm that specializes in resolving clients tax problems. I want the card to give the impression that we are not your typical stodgy accounting firm, but at the same time we will get the job done.
Industry/Entity Type
Business
Contact Information for Business Card
Dorian T Welsby
Certified Public Accountant
38-27 52nd Street
Sunnyside, NY 11287
Tel: (718) 555-0142
Fax: (888) 555-0199
e-mail: dtwthecpa@ledgerpost.com
website: harborfilingreliefexperts.com

```html
<!DOCTYPE html>
<html lang="en">
<head>
<meta charset="utf-8">
<title>Dorian T Welsby – Business Card</title>
<link rel="stylesheet" href="https://fonts.googleapis.com/css2?family=Tinos:ital,wght@0,400;1,400&display=swap">
<style>
  :root {
    --backdrop: #e4e4e8;
    --card: #ffffff;
    --ink: #111118;
    --accent: #3f3f9a;
    --navy: #26246f;
    --indigo: #5d5c9e;
    --lavender: #b9b8d6;
    --rule: #3a3890;
  }
  * { margin: 0; padding: 0; box-sizing: border-box; }
  html, body {
    width: 1200px;
    height: 900px;
    overflow: hidden;
    background: var(--backdrop);
    font-family: "Tinos", "Times New Roman", serif;
    color: var(--ink);
  }
  .card {
    position: absolute;
    left: 75px;
    top: 150px;
    width: 1050px;
    height: 600px;
    background: linear-gradient(160deg, #ffffff 0%, #f4f4f6 100%);
    box-shadow: 0 12px 40px rgba(0,0,0,0.18);
    overflow: hidden;
  }
  .hex-band {
    position: absolute;
    inset: 0;
    width: 100%;
    height: 100%;
  }
  .identity {
    position: absolute;
    right: 60px;
    top: 78px;
    text-align: right;
  }
  .identity .name {
    font-size: 38px;
    line-height: 1.1;
  }
  .identity .title {
    font-size: 32px;
    font-style: italic;
    line-height: 1.2;
  }
  .online {
    position: absolute;
    right: 60px;
    top: 180px;
    text-align: right;
    font-size: 30px;
    line-height: 1.25;
  }
  .label { color: var(--accent); }
  .divider {
    position: absolute;
    left: 400px;
    top: 230px;
    width: 2px;
    height: 140px;
    background: var(--rule);
  }
  .address {
    position: absolute;
    left: 40px;
    top: 280px;
    font-size: 31px;
    line-height: 1.18;
  }
</style>
</head>
<body>
  <article class="card">
    <svg class="hex-band" viewBox="0 0 1050 600" preserveAspectRatio="none" role="img" aria-label="Band of interlocking hexagons in navy, indigo and lavender rising from lower left to right">
      <defs>
        <linearGradient id="bandTone" x1="0" y1="1" x2="1" y2="0">
          <stop offset="0" stop-color="var(--navy)"/>
          <stop offset="0.5" stop-color="var(--indigo)"/>
          <stop offset="1" stop-color="var(--lavender)"/>
        </linearGradient>
      </defs>
      <polygon points="0,480 1050,270 1050,600 0,600" fill="url(#bandTone)"/>
    </svg>

    <header class="identity">
      <h1 class="name" style="font-weight:400">Dorian T Welsby</h1>
      <p class="title">Certified Public Accountant</p>
    </header>

    <div class="online">
      <p><span class="label">e-mail:</span> dtwthecpa@ledgerpost.com</p>
      <p><span class="label">website:</span> harborfilingreliefexperts.com</p>
    </div>

    <div class="divider"></div>

    <address class="address" style="font-style:normal">
      <p>38-27 52nd Street</p>
      <p>Sunnyside, NY 11287</p>
      <p><span class="label">Tel:</span> (718) 555-0142</p>
      <p><span class="label">Fax:</span> (888) 555-0199</p>
    </address>
  </article>
</body>
</html>
```